The Willow Cove Clinic - Instagram Photospot

We are looking for an instagram type wal for our pediatric dental office. We are thinking it could be weaved into a whole bunch of what we do (i.e. potentially water marked or faded in the background on letterhead, as an instragram type wall in the practice, as a banner or section of the home page on the website, on rack cards, etc.) I’m thinking it would utilize a nice fun cursive script for the wording "The Willow Cove Clinic is the spot for...." and a bunch of different sized “spots” with meaningful words that speak to who we are. That list would include things like:

• Fun
• Smiles
• Laughter
• Caring
• Comfort
• Amazing
• Kids
• Toddlers
• Teens
• Friends
• Family
• Health
• Education
• Cheer
• Positivity
• Exceptional Care

From a color perspective….we could look at a couple of options. We could have one version that has it washed out and in the background (more subliminal). We could have one version that was consistent with the colors in our logo. And we could have one version that popped with more color by utilizing the colors in some of the artwork we use throughout the office (snowboard picture as an example)

Target Market(s)

Appeal to hip families with kids

Industry/Entity Type

Pediatric Dental

Other font styles liked:
• something modern, hip, playful and fun

Colors
0054AA
0677BA
7BADD7
CADEEF
E8F1F8
0094D4
00A9DD
6FCCEA
C7EBF8
E9F6FB
00AB8E
00BBA5
67D7C9
C6EFE9
E9F9F6

Requirements
Must have
• Use of existing logo and a play on "spots" or polka dots with symbpolic wording. Must appeal to young parents and kiddos (including hip teens)
Should not have
• SHOULDNT BE OVER THE TOP KIDS.

```html
<!DOCTYPE html>
<html lang="en">
<head>
<meta charset="utf-8">
<title>The Willow Cove Clinic – Photo Spot Wall</title>
<link rel="stylesheet" href="https://fonts.googleapis.com/css2?family=Kalam:wght@700&family=Roboto+Condensed:wght@700&family=Open+Sans:wght@700&display=swap">
<style>
  :root {
    --navy: #1a3a4f;
    --dot-dark: #1f4459;
    --dot-mid: #4b7681;
    --dot-light: #dcddd3;
    --label: #7eb2c9;
    --label-light: #ffffff;
    --mint: #bfeeea;
    --aqua: #a9e2e6;
    --blush: #e7c7dd;
    --taupe: #cdb8bd;
    --paper: #f7fbfb;
    --bear-top: #d6e9f3;
    --bear-bottom: #7fb0cd;
  }
  * { margin: 0; padding: 0; box-sizing: border-box; }
  html, body { width: 1200px; height: 900px; overflow: hidden; background: var(--paper); }
  .spot-wall { position: relative; width: 1200px; height: 900px; overflow: hidden; }
  .wash-background {
    position: absolute; inset: 0;
    background:
      radial-gradient(ellipse 380px 260px at 20% 10%, var(--blush) 0%, transparent 70%),
      radial-gradient(ellipse 420px 300px at 85% 8%, var(--aqua) 0%, transparent 70%),
      radial-gradient(ellipse 360px 300px at 8% 55%, var(--mint) 0%, transparent 70%),
      radial-gradient(ellipse 420px 320px at 75% 60%, var(--blush) 0%, transparent 70%),
      radial-gradient(ellipse 460px 260px at 40% 95%, var(--mint) 0%, transparent 70%),
      radial-gradient(ellipse 300px 240px at 5% 20%, var(--taupe) 0%, transparent 70%),
      radial-gradient(ellipse 300px 220px at 95% 90%, var(--blush) 0%, transparent 70%),
      var(--paper);
  }
  .spot-layer { position: absolute; inset: 0; }
  .headline {
    font-family: "Kalam", cursive;
    font-weight: 700;
    font-size: 60px;
    fill: var(--navy);
  }
  .word-spot { fill: var(--navy); }
  .word-label {
    font-family: "Roboto Condensed", sans-serif;
    font-weight: 700;
    fill: var(--label);
    text-anchor: middle;
    dominant-baseline: central;
    letter-spacing: 1px;
  }
  .word-label--round { font-family: "Open Sans", sans-serif; }
  .dot-dark { fill: var(--dot-dark); }
  .dot-mid { fill: var(--dot-mid); }
  .dot-light { fill: var(--dot-light); opacity: 0.85; }
  .badge-spot { fill: var(--navy); }
  .badge-place {
    font-family: "Open Sans", sans-serif; font-weight: 700; font-size: 22px;
    fill: var(--label-light); text-anchor: middle; letter-spacing: 1px;
  }
</style>
</head>
<body>
<main class="spot-wall">
  <div class="wash-background" role="img" aria-label="Soft painterly splash texture in mint, aqua and blush tones"></div>

  <svg class="spot-layer" width="1200" height="900" viewBox="0 0 1418 1064" xmlns="http://www.w3.org/2000/svg">
    <defs>
      <linearGradient id="bear-wash" x1="0" y1="0" x2="0" y2="1">
        <stop offset="0" stop-color="var(--bear-top)"/>
        <stop offset="1" stop-color="var(--bear-bottom)"/>
      </linearGradient>
    </defs>

    <g class="scatter-dots">
      <circle class="dot-mid" cx="93" cy="42" r="20"/><circle class="dot-mid" cx="604" cy="35" r="20"/>
      <circle class="dot-mid" cx="996" cy="37" r="20"/><circle class="dot-mid" cx="1352" cy="56" r="27"/>
      <circle class="dot-mid" cx="351" cy="173" r="20"/><circle class="dot-mid" cx="239" cy="345" r="26"/>
      <circle class="dot-mid" cx="517" cy="355" r="26"/><circle class="dot-mid" cx="834" cy="332" r="26"/>
      <circle class="dot-mid" cx="1066" cy="357" r="26"/><circle class="dot-mid" cx="1200" cy="321" r="26"/>
      <circle class="dot-mid" cx="132" cy="465" r="26"/><circle class="dot-mid" cx="430" cy="536" r="26"/>
      <circle class="dot-mid" cx="934" cy="413" r="20"/><circle class="dot-mid" cx="1305" cy="417" r="20"/>
      <circle class="dot-mid" cx="940" cy="674" r="26"/><circle class="dot-mid" cx="1243" cy="702" r="26"/>
      <circle class="dot-mid" cx="1348" cy="653" r="26"/><circle class="dot-mid" cx="510" cy="744" r="26"/>
      <circle class="dot-mid" cx="692" cy="772" r="26"/><circle class="dot-mid" cx="962" cy="763" r="26"/>
      <circle class="dot-mid" cx="113" cy="989" r="26"/><circle class="dot-mid" cx="487" cy="988" r="20"/>
      <circle class="dot-mid" cx="766" cy="1019" r="20"/><circle class="dot-mid" cx="1036" cy="1011" r="20"/>
      <circle class="dot-mid" cx="1315" cy="1021" r="20"/><circle class="dot-mid" cx="209" cy="743" r="20"/>

      <circle class="dot-dark" cx="102" cy="273" r="26"/><circle class="dot-dark" cx="381" cy="284" r="26"/>
      <circle class="dot-dark" cx="632" cy="294" r="26"/><circle class="dot-dark" cx="929" cy="286" r="26"/>
      <circle class="dot-dark" cx="267" cy="553" r="26"/><circle class="dot-dark" cx="932" cy="556" r="26"/>
      <circle class="dot-dark" cx="1169" cy="596" r="26"/><circle class="dot-dark" cx="549" cy="848" r="26"/>
      <circle class="dot-dark" cx="829" cy="858" r="26"/><circle class="dot-dark" cx="1098" cy="851" r="26"/>
      <circle class="dot-dark" cx="1332" cy="808" r="26"/>

      <circle class="dot-light" cx="393" cy="40" r="20"/><circle class="dot-light" cx="786" cy="31" r="20"/>
      <circle class="dot-light" cx="620" cy="157" r="20"/><circle class="dot-light" cx="888" cy="149" r="20"/>
      <circle class="dot-light" cx="1168" cy="158" r="20"/><circle class="dot-light" cx="133" cy="378" r="26"/>
      <circle class="dot-light" cx="236" cy="432" r="26"/><circle class="dot-light" cx="602" cy="335" r="26"/>
      <circle class="dot-light" cx="962" cy="388" r="26"/><circle class="dot-light" cx="1338" cy="354" r="20"/>
      <circle class="dot-light" cx="1171" cy="428" r="20"/><circle class="dot-light" cx="60" cy="730" r="20"/>
      <circle class="dot-light" cx="968" cy="678" r="20"/><circle class="dot-light" cx="1247" cy="677" r="20"/>
      <circle class="dot-light" cx="1346" cy="740" r="26"/><circle class="dot-light" cx="312" cy="975" r="20"/>
      <circle class="dot-light" cx="589" cy="984" r="20"/><circle class="dot-light" cx="861" cy="977" r="20"/>
      <circle class="dot-light" cx="1138" cy="986" r="20"/><circle class="dot-light" cx="522" cy="720" r="20"/>
    </g>

    <text class="headline" x="710" y="122" text-anchor="middle" textLength="1190" lengthAdjust="spacingAndGlyphs">The Willow Cove Clinic is the spot for....</text>

    <g class="word-spots">
      <g transform="translate(226 222)"><circle class="word-spot" r="62"/><text class="word-label word-label--round" font-size="38" transform="rotate(-22)">FUN</text></g>
      <g transform="translate(501 205)"><circle class="word-spot" r="62"/><text class="word-label word-label--round" font-size="26" transform="rotate(40)">SMILES</text></g>
      <g transform="translate(774 225)"><circle class="word-spot" r="62"/><text class="word-label" font-size="24" transform="rotate(-15)">LAUGHTER</text></g>
      <g transform="translate(1053 235)"><circle class="word-spot" r="62"/><text class="word-label word-label--round" font-size="25">CARING</text></g>
      <g transform="translate(1294 218)"><circle class="word-spot" r="62"/><text class="word-label word-label--round" font-size="17" transform="rotate(45)">COMFORT</text></g>
      <g transform="translate(405 398)"><circle class="word-spot" r="62"/>
        <text class="word-label" font-size="20" transform="rotate(-15)"><tspan x="0" y="-13">EXCEPTIONAL</tspan><tspan x="0" y="15">CARE</tspan></text></g>
      <g transform="translate(1072 481)"><circle class="word-spot" r="62"/><text class="word-label" font-size="26" transform="rotate(70)">TODDLERS</text></g>
      <g transform="translate(1305 533)"><circle class="word-spot" r="62"/><text class="word-label word-label--round" font-size="30" transform="rotate(-60)">TEENS</text></g>
      <g transform="translate(133 621)"><circle class="word-spot" r="62"/><text class="word-label word-label--round" font-size="20">AMAZING</text></g>
      <g transform="translate(367 665)"><circle class="word-spot" r="62"/><text class="word-label word-label--round" font-size="38" transform="rotate(-45)">KIDS</text></g>
      <g transform="translate(1092 709)"><circle class="word-spot" r="62"/><text class="word-label word-label--round" font-size="19" transform="rotate(-145)">POSITIVITY</text></g>
      <g transform="translate(214 889)"><circle class="word-spot" r="62"/><text class="word-label word-label--round" font-size="20" transform="rotate(48)">FRIENDS</text></g>
      <g transform="translate(390 875)"><circle class="word-spot" r="62"/><text class="word-label word-label--round" font-size="28" transform="rotate(-32)">FAMILY</text></g>
      <g transform="translate(706 910)"><circle class="word-spot" r="62"/><text class="word-label word-label--round" font-size="28" transform="rotate(30)">HEALTH</text></g>
      <g transform="translate(976 902)"><circle class="word-spot" r="62"/><text class="word-label" font-size="24" transform="rotate(-72)">EDUCATION</text></g>
      <g transform="translate(1254 912)"><circle class="word-spot" r="62"/><text class="word-label word-label--round" font-size="30">CHEER</text></g>
    </g>

    <g class="place-badge" transform="translate(710 551)">
      <circle class="badge-spot" r="173"/>
      <ellipse cx="0" cy="-20" rx="125" ry="60" fill="url(#bear-wash)" role="img" aria-label="Watercolour bear illustration"/>
      <text class="badge-place" x="0" y="80">HARBOR FALLS, CA</text>
    </g>
  </svg>
</main>
</body>
</html>
```